Healthcare IT company looking for business card design

We develop IT systems for healthcare that significantly reduces cost and improves quality.

We want a business card design that is professional and clean, and using the colors in our logo.

Target Market(s)

Doctors and decision makers in the healthcare industry

Industry/Entity Type

Healthcare

Contact Information for Business Card

It should include
Name and title, address, telephone

Tobias Vrenholt, CEO
+46 712 418257
tobias@kelvaro.se

Font styles to use
Serif

Colors
0355a3
ed282f

Requirements
Must have
• Clean design
• Professional feel
Nice to have
• N/A
Should not have
• N/A

```html
<!DOCTYPE html>
<html lang="en">
<head>
<meta charset="utf-8">
<title>Kelvaro business card</title>
<link href="https://fonts.googleapis.com/css2?family=Open+Sans:wght@400;600;700&display=swap" rel="stylesheet">
<style>
  :root {
    --brand-blue: #1a5fb4;
    --brand-red: #ed282f;
    --ink: #222222;
    --card: #ffffff;
    --watermark: #f3f3f3;
    --backdrop: #ececec;
  }
  * { margin: 0; padding: 0; box-sizing: border-box; }
  html, body { width: 1200px; height: 1000px; overflow: hidden; }
  body {
    background: var(--backdrop);
    font-family: "Open Sans", Arial, sans-serif;
    color: var(--ink);
    position: relative;
  }
  .card {
    position: absolute;
    left: 265px;
    width: 666px;
    height: 397px;
    background: var(--card);
    box-shadow: 0 2px 8px rgba(0,0,0,0.18);
  }
  .card--front { top: 73px; }
  .card--back { top: 532px; }

  .wordmark {
    position: absolute;
    display: flex;
    align-items: flex-start;
    gap: 6px;
    color: var(--brand-blue);
    font-weight: 600;
    line-height: 1;
    letter-spacing: -1px;
  }
  .wordmark__dot {
    display: block;
    background: var(--brand-red);
    border-radius: 3px;
  }
  .card--front .wordmark { left: 30px; top: 30px; font-size: 92px; }
  .card--front .wordmark__dot { width: 22px; height: 22px; margin-top: 8px; }

  .watermark {
    position: absolute;
    left: 338px;
    top: 63px;
    width: 298px;
    height: 302px;
    background: var(--watermark);
    border-radius: 10px;
  }

  .person {
    position: absolute;
    left: 404px;
    top: 166px;
  }
  .person__name {
    color: var(--brand-blue);
    font-weight: 700;
    font-size: 20px;
    line-height: 26px;
    text-transform: uppercase;
  }
  .person__title { font-size: 18px; line-height: 24px; }

  .address {
    position: absolute;
    left: 33px;
    top: 188px;
    font-size: 15.5px;
    line-height: 25px;
    font-style: normal;
  }

  .contact-list {
    position: absolute;
    left: 33px;
    top: 270px;
    list-style: none;
    font-size: 15.5px;
    line-height: 24.3px;
  }
  .contact-list li { display: flex; align-items: center; gap: 7px; }
  .contact-list svg { width: 15px; height: 15px; fill: var(--brand-blue); flex: none; }

  .card--back .wordmark {
    left: 0; right: 0; top: 148px;
    justify-content: center;
    font-size: 112px;
  }
  .card--back .wordmark__dot { width: 26px; height: 26px; margin-top: 10px; }
  .back-url {
    position: absolute;
    left: 0; right: 0; top: 347px;
    text-align: center;
    font-size: 16px;
    letter-spacing: 1px;
  }
</style>
</head>
<body>
  <section class="card card--front">
    <div class="watermark" aria-hidden="true"></div>
    <div class="wordmark"><span>Kelvaro</span><span class="wordmark__dot"></span></div>

    <div class="person">
      <p class="person__name">Tobias Vrenholt</p>
      <p class="person__title">CEO</p>
    </div>

    <address class="address">
      1846 Marlow Ave., Suite C.<br>
      Fairhaven, OR. 97402
    </address>

    <ul class="contact-list">
      <li>
        <svg viewBox="0 0 16 16" aria-label="Phone"><path d="M1 6c0-2 3-4 7-4s7 2 7 4v1h-4V5.5H5V7H1zM4 8h8l2 3v3H2v-3zm4 1.5a1.5 1.5 0 1 0 0 3 1.5 1.5 0 0 0 0-3z"/></svg>
        <span>+ 000 000 0000</span>
      </li>
      <li>
        <svg viewBox="0 0 16 16" aria-label="Fax"><path d="M4 1h8v4H4zM1 6h14v6h-3v3H4v-3H1zm4 4v4h6v-4z"/></svg>
        <span>+ 000 000 0000</span>
      </li>
      <li>
        <svg viewBox="0 0 16 16" aria-label="Email"><path d="M1 3h14v1L8 9 1 4zm0 3 7 5 7-5v7H1z"/></svg>
        <span>info@kelvaro.com</span>
      </li>
      <li>
        <svg viewBox="0 0 16 16" aria-label="Website"><path d="M8 1a7 7 0 1 0 0 14A7 7 0 0 0 8 1zm0 2c1 1 1.6 2.4 1.7 4H6.3C6.4 5.4 7 4 8 3zM3.1 7a5 5 0 0 1 2.4-3.4C5 4.6 4.4 5.8 4.3 7zm0 2h1.2c.1 1.2.7 2.4 1.2 3.4A5 5 0 0 1 3.1 9zm3.2 0h3.4C9.6 10.6 9 12 8 13c-1-1-1.6-2.4-1.7-4zm5.4-2c-.1-1.2-.7-2.4-1.2-3.4A5 5 0 0 1 12.9 7z"/></svg>
        <span>www.kelvaro.com</span>
      </li>
    </ul>
  </section>

  <section class="card card--back">
    <div class="wordmark"><span>Kelvaro</span><span class="wordmark__dot"></span></div>
    <p class="back-url">www.kelvaro.com</p>
  </section>
</body>
</html>
```